Larkfield Crest Produce
Service full line of produce
http://www.quorvale.com/products/
http://www.brimelo.com/default.aspx
http://www.tavenhollowgroves.com/applepears
http://www.pellorridgeacres.com/index.php#
Dear Designers,
Below are some links to the logos I would like to have on my website..
I was unable to upload the logo..
http://www.odilyacrop.com/rnd.html
Dear ph,
Please check your private message...
thanks,
Zubin
TO SITE ADMIN,
WE CARRY SPECIFIC LABELS, CAN WE USE THEIR LOGOS ON THIS WEB DESIGN?
zubinmehrt- love the layout and bright colors... maybe need to change the pictures
KWTRL- I don't like the green u used.. also needs a little more contrast..
Hi,
-Gareth
ruhesh- i like that u used our logo.. can u make it bigger? also, y is everything in spanish? as for the picture, can u use more exotic fruits like lychee, longans, dragon fruits and guava along with the apples & oranges.. i like the picture very colorful.
What does it mean to Veil the project?

```html
<!DOCTYPE html>
<html lang="en">
<head>
<meta charset="utf-8">
<title>Larkfield Crest Produce</title>
<link rel="stylesheet" href="https://fonts.googleapis.com/css2?family=Arimo:wght@400;700&family=Roboto+Condensed:wght@700&display=swap">
<style>
:root{
  --green-top:#218d10;
  --green-deep:#0f6606;
  --yellow:#f6cf00;
  --orange:#f39200;
  --orange-dark:#d86a00;
  --red:#c8170c;
  --red-deep:#8f0c04;
  --brand-red:#d5160b;
  --text-grey:#6b6b6b;
  --white:#ffffff;
  --footer-green:#2f9a14;
  --footer-deep:#17640a;
}
*{box-sizing:border-box;margin:0;padding:0}
html,body{width:1200px;height:961px;overflow:hidden}
body{
  position:relative;
  font-family:"Arimo",Arial,sans-serif;
  background:linear-gradient(180deg,
    var(--green-top) 0,var(--green-deep) 118px,
    var(--yellow) 120px,var(--orange) 165px,
    var(--red) 215px,var(--red-deep) 824px,
    var(--footer-green) 826px,var(--footer-deep) 961px);
}
.abs{position:absolute}

/* brand tab */
.brand-tab{left:440px;top:0;width:320px;height:110px}
.brand{left:490px;top:30px;width:220px;display:flex;align-items:center;gap:8px}
.brand-dot{width:26px;height:26px;border-radius:50%;background:var(--brand-red);flex:none}
.brand-name{font-weight:700;color:var(--brand-red);font-size:19px;line-height:1.05}

/* navigation ribbon */
.nav{left:214px;top:100px;width:772px;height:44px}
.nav-links{left:250px;top:108px;width:700px;height:28px;display:flex;justify-content:space-between;align-items:center;list-style:none}
.nav-links li{font-size:12.5px;font-weight:700;color:var(--white);padding:7px 12px;text-transform:uppercase}
.nav-links li.active{background:var(--red);border-radius:2px;box-shadow:inset 0 0 0 1px rgba(0,0,0,.15)}
.nav-links li.faq{text-transform:none}

/* hero */
.hero{left:208px;top:152px;width:787px;height:262px;border:3px solid var(--white);box-shadow:0 2px 6px rgba(0,0,0,.35);overflow:hidden}
.hero-photo{position:absolute;inset:0;background:
  radial-gradient(circle at 20% 30%,#d6402a 0,transparent 30%),
  radial-gradient(circle at 55% 40%,#f2b21c 0,transparent 30%),
  radial-gradient(circle at 85% 30%,#c42a3a 0,transparent 30%),
  radial-gradient(circle at 40% 85%,#7aa61e 0,transparent 35%),
  linear-gradient(135deg,#8a2a14,#c6471c 40%,#6e8a1a)}
.hero-truck{position:absolute;left:500px;top:140px;width:130px;height:62px;border-radius:6px;background:linear-gradient(180deg,#f0f0f0,#b8b8b8)}
.hero-title{position:absolute;left:18px;top:170px;font-family:"Roboto Condensed",Arial,sans-serif;font-size:30px;color:var(--brand-red);text-shadow:0 0 3px #fff,0 0 3px #fff}
.hero-strip{position:absolute;left:0;top:208px;width:560px;height:22px;background:rgba(0,0,0,.55);color:var(--white);font-size:12px;font-weight:700;padding:4px 18px}
.hero-dots{position:absolute;right:10px;bottom:10px;display:flex;gap:4px}
.hero-dots span{width:11px;height:11px;background:#fff;border:1px solid #777}
.hero-dots span.on{background:#444}

/* info boxes */
.info{top:436px;width:247px;height:195px;background:var(--white);border-radius:6px;box-shadow:0 2px 5px rgba(0,0,0,.35)}
.info-head{position:absolute;left:-6px;top:-8px;width:150px;height:36px;background:linear-gradient(180deg,var(--yellow),var(--orange));border-radius:3px;display:flex;align-items:center;gap:8px;padding-left:10px;box-shadow:0 2px 3px rgba(0,0,0,.3)}
.info-icon{width:24px;height:24px;border-radius:50%;background:var(--white);border:3px solid var(--brand-red)}
.info-head h2{font-family:"Roboto Condensed",Arial,sans-serif;font-size:19px;color:var(--white);text-shadow:0 1px 1px rgba(0,0,0,.35)}
.info-body{position:absolute;left:14px;top:40px;right:14px;font-size:10.5px;line-height:1.45;color:var(--text-grey)}
.info-body p{margin-bottom:8px}
.read-more{color:var(--brand-red);font-weight:700}
.contact-list{list-style:none}
.contact-list li{display:flex;align-items:flex-start;gap:7px;margin-bottom:3px}
.contact-list svg{flex:none;margin-top:1px}

/* products */
.products{left:208px;top:662px;width:787px;height:142px;background:var(--white);border-radius:6px;box-shadow:0 2px 5px rgba(0,0,0,.35)}
.arrow{top:712px;width:26px;height:36px;background:linear-gradient(180deg,#3aa51a,#1b6e0c);border-radius:3px}
.arrow-left{left:206px}
.arrow-right{left:969px}
.product-row{left:245px;top:678px;width:715px;display:flex;justify-content:space-between}
.product{width:90px;text-align:center}
.product-img{width:76px;height:64px;margin:0 auto 14px;border-radius:50%}
.product-name{font-size:11.5px;font-weight:700;color:var(--brand-red)}

/* footer */
.footer-follow{left:330px;top:850px;width:190px;text-align:right;color:var(--white);font-size:10px}
.follow-row{display:flex;justify-content:flex-end;align-items:center;gap:4px;margin-bottom:14px;font-weight:700;color:var(--yellow)}
.social{width:22px;height:22px;border-radius:3px;background:#3b6fc4}
.social.alt{background:#39a6e0}
.footer-follow p{margin-bottom:6px}
.divider{top:845px;width:1px;height:98px;background:rgba(255,255,255,.35)}
.subscribe{left:556px;top:849px;width:210px}
.footer-head{font-size:11px;font-weight:700;color:var(--yellow);margin-bottom:8px}
.field{height:20px;background:#eaf5d8;border:1px solid #b6d88a;font-size:10px;color:#666;padding:3px 6px;margin-bottom:6px}
.btn{display:inline-block;background:linear-gradient(180deg,var(--yellow),var(--orange-dark));color:#5a1a00;font-size:11px;font-weight:700;padding:4px 10px;border-radius:3px}
.call{left:812px;top:849px;width:190px}
.call .footer-head{text-align:center}
.call-row{display:flex;align-items:center;gap:8px;color:var(--white)}
.call-icon{width:36px;height:36px;border-radius:50%;background:var(--white);display:flex;align-items:center;justify-content:center;flex:none}
.call-label{font-size:15px;font-weight:700}
.call-number{font-family:"Roboto Condensed",Arial,sans-serif;font-size:23px}
</style>
</head>
<body>

<svg class="abs brand-tab" viewBox="0 0 320 110" aria-hidden="true">
  <path d="M0 0 H320 C300 0 290 18 288 50 C286 90 270 100 240 100 H80 C50 100 34 90 32 50 C30 18 20 0 0 0 Z" fill="#ffffff"/>
</svg>
<div class="abs brand">
  <span class="brand-dot"></span>
  <span class="brand-name">Larkfield Crest<br>Produce</span>
</div>

<svg class="abs nav" viewBox="0 0 772 44" preserveAspectRatio="none" aria-hidden="true">
  <defs><linearGradient id="rib" x1="0" y1="0" x2="0" y2="1"><stop offset="0" stop-color="#f9d200"/><stop offset="1" stop-color="#ee8a00"/></linearGradient></defs>
  <path d="M0 8 H30 V44 H0 L10 26 Z" fill="#c86a00"/>
  <path d="M772 8 H742 V44 H772 L762 26 Z" fill="#c86a00"/>
  <rect x="18" y="2" width="736" height="36" fill="url(#rib)"/>
</svg>
<ul class="abs nav-links">
  <li class="active">Home</li><li>About Us</li><li>Our Products</li><li>Our Services</li><li>Contact Us</li><li>Support</li><li class="faq">FAQs</li>
</ul>

<section class="abs hero">
  <div class="hero-photo" role="img" aria-label="Photo of colourful exotic fruits: rambutan, dragon fruit, lychee, star fruit and oranges"></div>
  <div class="hero-truck" role="img" aria-label="Illustration of a delivery truck"></div>
  <h1 class="hero-title">A full line fruit distributor</h1>
  <div class="hero-strip">we offer one of the largest varieties of year-round and seasonal fruit</div>
  <div class="hero-dots"><span class="on"></span><span></span><span></span></div>
</section>

<section class="abs info" style="left:208px">
  <div class="info-head"><span class="info-icon"></span><h2>Who We Are</h2></div>
  <div class="info-body">
    <p>Your data regarding this section goes here. Your data regarding this section goes here. Your data regarding this section goes here.</p>
    <p>Your data regarding this section goes here. Your data regarding this section goes here. Your data regarding this section goes here.</p>
    <span class="read-more">read more</span>
  </div>
</section>

<section class="abs info" style="left:475px">
  <div class="info-head"><span class="info-icon"></span><h2>What We Do</h2></div>
  <div class="info-body">
    <p>Your data regarding this section goes here. Your data regarding this section goes here. Your data regarding this section goes here.</p>
    <p>Your data regarding this section goes here. Your data regarding this section goes here. Your data regarding this section goes here.</p>
    <span class="read-more">read more</span>
  </div>
</section>

<section class="abs info" style="left:745px">
  <div class="info-head"><span class="info-icon"></span><h2>Contact Us</h2></div>
  <div class="info-body">
    <ul class="contact-list">
      <li><svg width="12" height="10" viewBox="0 0 12 10"><rect x=".5" y=".5" width="11" height="9" fill="none" stroke="#555"/><path d="M.5 .5 6 5 11.5 .5" fill="none" stroke="#555"/></svg>Email : info@yourdomain.com</li>
      <li><svg width="12" height="12" viewBox="0 0 12 12"><path d="M2 1 4 1 5 4 3.5 5 C4 7 5 8 7 8.5 L8 7 11 8 11 10 C6 11 1 6 2 1Z" fill="#555"/></svg>Phone : 123 456 7890</li>
      <li><svg width="12" height="12" viewBox="0 0 12 12"><circle cx="6" cy="6" r="5.5" fill="#39a6e0"/></svg>Chat : your chat name</li>
      <li><svg width="12" height="12" viewBox="0 0 12 12"><rect width="12" height="12" rx="2" fill="#3b6fc4"/></svg>Social : yourpagename</li>
      <li><svg width="12" height="12" viewBox="0 0 12 12"><path d="M6 0 C3 0 1.5 2 1.5 4.5 C1.5 7.5 6 12 6 12 C6 12 10.5 7.5 10.5 4.5 C10.5 2 9 0 6 0Z" fill="#555"/></svg>Your Address goes here your address goes here your address goes here</li>
    </ul>
  </div>
</section>

<div class="abs products"></div>
<div class="abs arrow arrow-left"><svg width="26" height="36" viewBox="0 0 26 36"><path d="M16 10 9 18 16 26" fill="none" stroke="#fff" stroke-width="3"/></svg></div>
<div class="abs arrow arrow-right"><svg width="26" height="36" viewBox="0 0 26 36"><path d="M10 10 17 18 10 26" fill="none" stroke="#fff" stroke-width="3"/></svg></div>
<div class="abs product-row">
  <div class="product"><div class="product-img" role="img" aria-label="Raspberries" style="background:radial-gradient(circle,#e2405a,#a81830)"></div><div class="product-name">Product Name</div></div>
  <div class="product"><div class="product-img" role="img" aria-label="Watermelon slice" style="background:radial-gradient(circle,#e8402a 45%,#3d8f1c 70%)"></div><div class="product-name">Product Name</div></div>
  <div class="product"><div class="product-img" role="img" aria-label="Blood oranges" style="background:radial-gradient(circle,#e0602a,#a52810)"></div><div class="product-name">Product Name</div></div>
  <div class="product"><div class="product-img" role="img" aria-label="Orange slices" style="background:radial-gradient(circle,#ffb53a,#f07c00)"></div><div class="product-name">Product Name</div></div>
  <div class="product"><div class="product-img" role="img" aria-label="Red apples" style="background:radial-gradient(circle,#f0a060,#c41a10)"></div><div class="product-name">Product Name</div></div>
  <div class="product"><div class="product-img" role="img" aria-label="Strawberries" style="background:radial-gradient(circle,#f0402a,#b01010)"></div><div class="product-name">Product Name</div></div>
  <div class="product"><div class="product-img" role="img" aria-label="Peaches" style="background:radial-gradient(circle,#f8c050,#e05a20)"></div><div class="product-name">Product Name</div></div>
</div>

<footer>
  <div class="abs footer-follow">
    <div class="follow-row">Follow Us on <span class="social"></span><span class="social alt"></span><span class="social"></span></div>
    <p>About Us &nbsp;|&nbsp; Privacy Policy &nbsp;|&nbsp; Terms and Conditions</p>
    <p><strong>© 2012, Company Name Goes here. All rights reserved</strong></p>
  </div>
  <div class="abs divider" style="left:535px"></div>
  <div class="abs subscribe">
    <div class="footer-head">Subscribe for Updates</div>
    <div class="field">Your Name Goes Here</div>
    <div class="field">Your Email Goes Here</div>
    <span class="btn">Subscribe</span>
  </div>
  <div class="abs divider" style="left:786px"></div>
  <div class="abs call">
    <div class="footer-head">For any kind of Query</div>
    <div class="call-row">
      <span class="call-icon"><svg width="20" height="20" viewBox="0 0 12 12"><path d="M2 1 4 1 5 4 3.5 5 C4 7 5 8 7 8.5 L8 7 11 8 11 10 C6 11 1 6 2 1Z" fill="#2f9a14"/></svg></span>
      <div><div class="call-label">Call to Action</div><div class="call-number">123 456 7890</div></div>
    </div>
  </div>
</footer>

</body>
</html>
```